UI for Online Code Editor

I need a UI design for an online code editor called Quillmoor.

Quillmoor is an online code editor for web developers, that aims to be an intuitive and beautiful editor that you can use on any device or browser. The current prototype can be viewed at http://quillmoor.example/editor

I am completely open to different colours and UI approaches, feel free to invent a new way for people to code :)

The final design should be something that is clean, elegant and functional. I will favour designs that are genuinely nice to look at and have a 'mac app' polished feel to them.

I have uploaded a psd that will provide a basic idea.

Go crazy, All ideas will be considered.
Updates

Target Market(s)

Web Developers

Industry/Entity Type

Online

Requirements
Must have
• -Tabs: similar to chrome tabs, for different files.
-Line numbers
-The editor text area
Nice to have
• -An expandable/contractible file manager, on either side of the editor.
-Related files area under tabs. This is for quick access to files that have been included in the users code (ie jquery.js, etc). This will likely be expandable/contractable.

```html
<!DOCTYPE html>
<html lang="en">
<head>
<meta charset="utf-8">
<title>Quillmoor — Online Code Editor</title>
<link rel="stylesheet" href="https://fonts.googleapis.com/css2?family=Arimo:wght@400;700&display=swap">
<style>
  :root {
    --navy: #04306a;
    --brand: #0b3a78;
    --white: #ffffff;
    --sky: #0ba3f0;
    --tab-active-top: #3b78b8;
    --tab-active-bottom: #1b4f8c;
    --tab-idle-top: #ffffff;
    --tab-idle-bottom: #dcdcdc;
    --pill: #d4dce6;
    --pill-text: #1b2d48;
    --gutter: #e8e8e8;
    --gutter-text: #1d2f4a;
    --code-bg: #021a36;
    --c-doctype: #1ea3ea;
    --c-tag: #ff5b1e;
    --c-prop: #56d84a;
    --c-text: #ffffff;
    --status: #6b6b6b;
    --footer-text: #b3c3d8;
  }
  * { box-sizing: border-box; margin: 0; padding: 0; }
  html, body { width: 1200px; height: 1002px; overflow: hidden; }
  body {
    position: relative;
    background: var(--navy);
    font-family: "Arimo", Arial, sans-serif;
  }
  .app-header {
    position: absolute; left: 0; top: 0; width: 1200px; height: 86px;
    background: var(--white);
  }
  .brand {
    position: absolute; left: 107px; top: 30px;
    font-size: 24px; font-weight: 700; color: var(--brand);
    letter-spacing: 0.3px;
  }
  .window-actions {
    position: absolute; left: 1004px; top: 52px;
    display: flex; gap: 4px;
  }
  .settings-button {
    position: absolute; left: 976px; top: 86px; width: 120px; height: 35px;
    background: var(--sky); border-radius: 0 0 6px 6px;
    display: flex; align-items: center; gap: 10px; padding-left: 13px;
    color: var(--white); font-size: 12px; font-weight: 700;
  }
  .project-tabs { position: absolute; left: 96px; top: 106px; display: flex; gap: 1px; }
  .project-tab {
    position: relative; width: 150px; height: 44px; border-radius: 7px 7px 0 0;
    font-size: 12px; font-weight: 700; padding: 17px 0 0 19px;
  }
  .project-tab .close { position: absolute; right: 10px; top: 5px; font-size: 12px; }
  .project-tab.is-active {
    background: linear-gradient(var(--tab-active-top), var(--tab-active-bottom));
    color: var(--white);
  }
  .project-tab.is-idle {
    width: 151px;
    background: linear-gradient(var(--tab-idle-top), var(--tab-idle-bottom));
    color: var(--brand); padding-left: 21px;
  }
  .workspace {
    position: absolute; left: 96px; top: 152px; width: 1000px; height: 743px;
    background: var(--white);
    box-shadow: 0 0 8px 2px rgba(255,255,255,0.55);
  }
  .file-pills { position: absolute; left: 13px; top: 13px; display: flex; gap: 11px; }
  .file-pill {
    height: 24px; width: 82px; border-radius: 10px; background: var(--pill);
    color: var(--pill-text); font-size: 13px; line-height: 24px; text-align: center;
  }
  .editor {
    position: absolute; left: 10px; top: 46px; width: 973px; height: 647px;
    background: var(--code-bg); display: flex;
  }
  .gutter { width: 52px; height: 100%; background: var(--gutter); padding-top: 50px; }
  .gutter span {
    display: block; height: 28px; line-height: 16px;
    font-size: 13px; color: var(--gutter-text); text-align: center; padding-right: 2px;
  }
  .code { padding: 50px 0 0 34px; font-size: 13px; }
  .code div { height: 28px; line-height: 16px; white-space: pre; }
  .i1 { padding-left: 36px; } .i2 { padding-left: 72px; } .i3 { padding-left: 108px; }
  .doctype { color: var(--c-doctype); }
  .tag { color: var(--c-tag); }
  .prop { color: var(--c-prop); }
  .txt { color: var(--c-text); }
  .status-bar {
    position: absolute; left: 65px; right: 21px; top: 700px;
    display: flex; justify-content: space-between;
    font-size: 13px; color: var(--status);
  }
  .app-footer {
    position: absolute; left: 119px; top: 930px;
    font-size: 12px; line-height: 14px; color: var(--footer-text);
  }
  .app-footer nav span { margin: 0 6px; }
</style>
</head>
<body>
  <header class="app-header">
    <div class="brand">QUILLMOOR</div>
    <div class="window-actions">
      <svg width="28" height="28" viewBox="0 0 28 28" aria-label="Minimise">
        <rect x="1.5" y="1.5" width="25" height="25" rx="4" fill="#fff" stroke="#000" stroke-width="3"/>
        <line x1="1.5" y1="8" x2="26.5" y2="8" stroke="#000" stroke-width="2"/>
        <circle cx="5" cy="5" r="1" fill="#000"/><circle cx="8" cy="5" r="1" fill="#000"/>
        <rect x="7" y="15" width="14" height="3.5" fill="#000"/>
      </svg>
      <svg width="28" height="28" viewBox="0 0 28 28" aria-label="New window">
        <rect x="1.5" y="1.5" width="25" height="25" rx="4" fill="#fff" stroke="#000" stroke-width="3"/>
        <line x1="1.5" y1="8" x2="26.5" y2="8" stroke="#000" stroke-width="2"/>
        <circle cx="5" cy="5" r="1" fill="#000"/><circle cx="8" cy="5" r="1" fill="#000"/>
        <rect x="7" y="15" width="14" height="3.5" fill="#000"/>
        <rect x="12.25" y="10" width="3.5" height="14" fill="#000"/>
      </svg>
      <svg width="28" height="28" viewBox="0 0 28 28" aria-label="Save">
        <rect x="1.5" y="1.5" width="25" height="25" rx="4" fill="#fff" stroke="#000" stroke-width="3"/>
        <polyline points="7,14 12,19 21,9" fill="none" stroke="#000" stroke-width="3.5"/>
      </svg>
    </div>
  </header>

  <div class="settings-button">
    <svg width="18" height="18" viewBox="0 0 18 18" aria-hidden="true">
      <circle cx="9" cy="9" r="8.5" fill="#0a2340"/>
      <circle cx="9" cy="9" r="4.6" fill="none" stroke="#0ba3f0" stroke-width="2.2" stroke-dasharray="2 1.6"/>
      <circle cx="9" cy="9" r="1.8" fill="#0ba3f0"/>
    </svg>
    SETTINGS
  </div>

  <div class="project-tabs">
    <div class="project-tab is-active">Project Name<span class="close">X</span></div>
    <div class="project-tab is-idle">Project Name<span class="close">X</span></div>
  </div>

  <main class="workspace">
    <div class="file-pills">
      <div class="file-pill">index.html</div>
      <div class="file-pill">style.css</div>
    </div>

    <section class="editor">
      <div class="gutter">
        <span>1</span><span>2</span><span>3</span><span>4</span><span>5</span>
        <span>6</span><span>7</span><span>8</span><span>9</span><span>10</span>
        <span>11</span><span>12</span><span>13</span><span>14</span><span>15</span>
        <span>16</span><span>17</span><span>18</span><span>19</span>
      </div>
      <div class="code">
        <div class="doctype">&lt;!doctype html&gt;</div>
        <div class="tag">&lt;html&gt;</div>
        <div class="tag i1">&lt;head&gt;</div>
        <div class="tag i1">&lt;style&gt;</div>
        <div class="tag i2">h1{</div>
        <div class="prop i3">font-family: Helvetica, Arial;</div>
        <div class="prop i3">text-align: center;</div>
        <div class="tag i2">}</div>
        <div class="tag i1">&lt;/style&gt;</div>
        <div class="tag i1">&lt;/head&gt;</div>
        <div class="tag i1">&lt;body&gt;</div>
        <div class="i2"><span class="tag">&lt;h1&gt;</span><span class="txt">Welcome to Quillmoor</span><span class="tag">&lt;/h1&gt;</span></div>
        <div class="i2"><span class="tag">&lt;p&gt;</span><span class="txt">Prefer your own colours?</span><span class="tag">&lt;/p&gt;</span></div>
        <div class="i2"><span class="tag">&lt;p&gt;</span><span class="txt">Roll your own by clicking settings and inserting some css.</span><span class="tag">&lt;/p&gt;</span></div>
        <div class="i2"><span class="tag">&lt;p&gt;</span><span class="txt">PRO TIP: use f2, f3, f4 to toggle the different modes</span><span class="tag">&lt;/p&gt;</span></div>
        <div class="tag i1">&lt;script&gt;</div>
        <div class="tag i1">&lt;/script&gt;</div>
        <div class="tag i1">&lt;/body&gt;</div>
        <div class="doctype">&lt;/html&gt;</div>
      </div>
    </section>

    <div class="status-bar">
      <span>Globals: 0</span>
      <span>Row: 7 Col: 22 Total: 102</span>
    </div>
  </main>

  <footer class="app-footer">
    <p>Copyright 2013. All rights reserved.</p>
    <nav>Terms &amp; Conditions<span>-</span>Privacy<span>-</span>Disclaimer</nav>
  </footer>
</body>
</html>
```